Wellness Coach/Personal trainer needs wordpress site/blog with ecommerce capable membership area

We need a WordPress design for FiveCoinCoach.com. This is a blog about wellness, weight loss, and health related topics. Design logo will be provided to the winner.

A great site with a design that we would like to emulate are http://qv4.org. The design should be simple, clean, unique, fun, and distinctive. Above all, it should be highly readable and easy to navigate.

These are the specific sections/categories of the blog that should be included and incorporated into the design SEE BELOW.

Thanks in advance for your consideration

Project Deadline Extended
Reason: I have extended the deadline to evaluate more designs from other pros

Hello all, Please take a minute to review the requirements for this project and please make sure you are capable of meeting ALL the requirements. As you already know I will be making a decision very shortly on whose design I will be moving forward with, if there are any last minute submissions now is the time. Thank you for your time.

Target Market(s)

90 % women 10 % men my clients are usually professionals who value their appearance, health, longevity and time.

Industry/Entity Type

Personal Trainer

Font styles to use
Serif

Colors
886aae
ffcf3e

Requirements
Must have
• Requirements

- start losing weight today.... 555 219 6847 (first line)
- visuals/images and backgrounds to give the idea of wellness, weight loss, healthy living, etc
- navigation menu - home, who we are, what we do, who we serve, blog, contact, members area

1) slider element at top below navigation menu
2) slider element near bottom of page will have testimonials
3) contact form/inquiry form (one page)
4) will provide wellness logo (to give credibility)
5) color scheme purple, gold and white
6) membership area
7) fb, tw, youtube icons
8) footer area - In the footer, there will be smaller company logo, copyright,
disclaimer, privacy policy, terms n conditions, verse of day, and contact info, Phone: (555) 219-6847
Email: support@...
Address:
9) use dummy content/graphic as they will be replaced by real content (the winner will provide instruction on how to make changes to all text and changing graphics)
9) ecommerce enabled / newsletter signup area

```html
<!DOCTYPE html>
<html lang="en">
<head>
<meta charset="utf-8">
<title>FiveCoinCoach – Personal Training</title>
<link href="https://fonts.googleapis.com/css2?family=Lora:wght@400;500;700&family=Playfair+Display:wght@400;700&display=swap" rel="stylesheet">
<style>
  :root {
    --hero-dark: #0d0a12;
    --hero-mid: #3a3146;
    --white: #ffffff;
    --ink: #1f1c26;
    --muted: #86828e;
    --purple: #886aae;
    --purple-deep: #6d5291;
    --gold: #ffcf3e;
  }
  * { box-sizing: border-box; margin: 0; padding: 0; }
  html, body { width: 1200px; height: 1122px; overflow: hidden; background: var(--white); }
  body { position: relative; font-family: "Lora", Georgia, serif; color: var(--ink); }

  .hero { position: absolute; left: 0; top: 0; width: 1200px; height: 609px; overflow: hidden; }
  .hero-photo {
    position: absolute; inset: 0;
    background:
      radial-gradient(ellipse 330px 420px at 280px 360px, #8a7366 0%, #4a3c42 38%, rgba(20,16,26,0) 75%),
      radial-gradient(ellipse 600px 500px at 700px 300px, var(--hero-mid) 0%, var(--hero-dark) 80%);
  }

  .topbar { position: absolute; top: 10px; left: 0; width: 100%; font: 400 10px "Lora", serif; color: var(--white); }
  .lang-list { position: absolute; left: 92px; display: flex; gap: 12px; }
  .lang-list .active { text-decoration: underline; }
  .sign-in { position: absolute; left: 1060px; letter-spacing: .5px; }

  .brand { position: absolute; left: 102px; top: 142px; display: flex; align-items: center; gap: 10px; }
  .brand-dot { width: 50px; height: 50px; border-radius: 50%; background: var(--purple); }
  .brand-name { font: 700 26px "Lora", serif; color: var(--white); }

  .main-nav { position: absolute; left: 420px; top: 160px; display: flex; gap: 15px; font: 400 11px "Lora", serif; color: var(--white); text-transform: uppercase; letter-spacing: .2px; }
  .main-nav .current { color: var(--gold); }
  .shop-tools { position: absolute; left: 996px; top: 155px; display: flex; align-items: center; gap: 14px; color: var(--white); font: 700 12px "Lora", serif; }

  .hero-copy { position: absolute; right: 194px; top: 284px; text-align: right; color: var(--white); }
  .hero-kicker { font: 400 13px "Lora", serif; letter-spacing: .4px; text-transform: uppercase; color: var(--gold); }
  .hero-title { margin-top: 12px; font: 400 40px/48px "Playfair Display", serif; text-transform: uppercase; }
  .hero-note { margin-top: 14px; font: 400 12px/20px "Lora", serif; color: #cfc8d8; }
  .hero-actions { margin-top: 20px; display: flex; justify-content: flex-end; gap: 9px; }
  .btn-outline { display: flex; align-items: center; justify-content: center; height: 33px; padding: 0 24px; border: 2px solid var(--white); color: var(--white); font: 700 11px "Lora", serif; text-transform: uppercase; }
  .btn-outline.primary { background: var(--purple); border-color: var(--purple); }

  .about { position: absolute; top: 609px; left: 0; width: 1200px; text-align: center; }
  .about-title { margin-top: 89px; font: 400 28px "Playfair Display", serif; letter-spacing: .5px; color: var(--ink); }
  .about-rule { width: 46px; height: 3px; background: var(--purple); margin: 18px auto 0; }
  .about-lead { width: 960px; margin: 20px auto 0; font: 400 17px/28px "Lora", serif; color: var(--muted); }

  .services { position: absolute; top: 870px; left: 0; width: 1200px; }
  .service { position: absolute; width: 230px; text-align: center; }
  .service-icon { width: 96px; height: 96px; border-radius: 50%; background: var(--gold); margin: 0 auto; display: flex; align-items: center; justify-content: center; }
  .service-name { margin-top: 22px; font: 500 15px "Lora", serif; color: var(--purple-deep); text-transform: uppercase; }
  .service-text { margin-top: 6px; font: 400 12px/21px "Lora", serif; color: var(--muted); }

  .contact-tab { position: absolute; left: 888px; bottom: 0; width: 264px; height: 36px; background: var(--purple); color: var(--white); font: 400 13px "Lora", serif; display: flex; align-items: center; justify-content: space-between; padding: 0 14px; }
</style>
</head>
<body>
  <header class="hero">
    <div class="hero-photo" role="img" aria-label="Photo of a fit woman in a sports top lifting a chrome dumbbell against a dark background"></div>

    <div class="topbar">
      <div class="lang-list"><span class="active">EN</span><span>FR</span><span>GE</span><span>I</span><span>€</span><span>$</span></div>
      <div class="sign-in">SIGN IN</div>
    </div>

    <div class="brand"><span class="brand-dot"></span><span class="brand-name">PocketPaceFit</span></div>

    <nav class="main-nav">
      <span class="current">Home</span><span>Who We Are</span><span>What We Do</span><span>Who We Serve</span><span>Blog</span><span>Contact</span><span>Members Area</span>
    </nav>

    <div class="shop-tools">
      <svg width="14" height="14" viewBox="0 0 14 14" aria-label="Search"><circle cx="6" cy="6" r="4.5" fill="none" stroke="#fff" stroke-width="2"/><line x1="9.3" y1="9.3" x2="13" y2="13" stroke="#fff" stroke-width="2"/></svg>
      <svg width="16" height="18" viewBox="0 0 16 18" aria-label="Cart"><path d="M5 5V4a3 3 0 0 1 6 0v1" fill="none" stroke="#fff" stroke-width="1.6"/><rect x="1" y="5" width="14" height="12" fill="#fff"/></svg>
      <span>$0.00</span>
    </div>

    <div class="hero-copy">
      <p class="hero-kicker">Getting in shape just got more affordable</p>
      <h1 class="hero-title">Start losing weight today<br>Call us at 555.219.6847</h1>
      <p class="hero-note">Couples that train together stay together.<br>Ask us abouy our couples special.</p>
      <div class="hero-actions">
        <span class="btn-outline primary">Shop Now</span>
        <span class="btn-outline">Feature</span>
      </div>
    </div>
  </header>

  <section class="about">
    <h2 class="about-title">FEW WORDS ABOUT US</h2>
    <div class="about-rule"></div>
    <p class="about-lead">We focus on heart rate, rate of perceived exertion, strength in movement, balance, agility and dexterity not to mention building a strong, solid core.</p>
  </section>

  <section class="services">
    <div class="service" style="left:101px">
      <div class="service-icon"><svg width="40" height="40" viewBox="0 0 40 40"><path d="M8 22l10 10 16-22" fill="none" stroke="#fff" stroke-width="5" stroke-linejoin="round"/></svg></div>
      <h3 class="service-name">Group Personal Training</h3>
      <p class="service-text">It's designed to get you fit enough for life's adventures, shed excess weight and build lasting energy.</p>
    </div>
    <div class="service" style="left:343px">
      <div class="service-icon"><svg width="40" height="40" viewBox="0 0 40 40"><path d="M8 32c0-12 8-18 18-18V8l10 10-10 10v-6c-8 0-14 3-18 10z" fill="#fff"/></svg></div>
      <h3 class="service-name">Trek Training</h3>
      <p class="service-text">The TrailReady program will prepare you for trekking and high altitude with the right endurance.</p>
    </div>
    <div class="service" style="left:597px">
      <div class="service-icon"><svg width="40" height="40" viewBox="0 0 40 40"><rect x="6" y="18" width="7" height="16" fill="#fff"/><path d="M15 18l7-11c3 0 4 2 3 5l-1 5h9c2 0 3 2 2 4l-3 10c-1 2-2 3-4 3H15z" fill="#fff"/></svg></div>
      <h3 class="service-name">Rotating Fitness Classes</h3>
      <p class="service-text">Cardio training, Conditioning, Strength training, and Boxing/Kickboxing – give you variety every week.</p>
    </div>
    <div class="service" style="left:855px">
      <div class="service-icon"><svg width="40" height="40" viewBox="0 0 40 40"><circle cx="20" cy="20" r="15" fill="#fff"/><rect x="18" y="10" width="4" height="13" fill="#ffcf3e"/><circle cx="20" cy="28" r="2.4" fill="#ffcf3e"/></svg></div>
      <h3 class="service-name">Strength Training</h3>
      <p class="service-text">Our Strength training program will help you build muscle, protect joints and move well.</p>
    </div>
  </section>

  <div class="contact-tab">
    <span>Contact us</span>
    <svg width="18" height="12" viewBox="0 0 18 12"><ellipse cx="7" cy="5" rx="7" ry="5" fill="#fff"/><ellipse cx="12" cy="7" rx="6" ry="4.5" fill="#e4dbef"/></svg>
  </div>
</body>
</html>
```